Modern Web Design for Nonprofit Organization

Our client is looking to redesign their website. They want a modern look, clean and professional, that integrates their new brand guidelines.

Here is clients current site:
http://www.valorandes.org/

They want their own unique design but here are some sites the clients likes:
https://www.brixtonvane.com/en/
https://oakhollowrise.org/
https://www.lumacraft.com/
https://www.tbnlawgroup.com/
https://www.greyharborco.org/

Attached please find the clients logos, color palette, site plan and design specs.

You will create a homepage mockup that will have the following sections in this order:
1. Thin Alert Bar at very top with one line message
2. Nav Bar with Logo and Main Nav (red in site plan)
3. Hero Image or Video
4. Signup Bar with name email and zip and connect button
5. Intro section with image, welcome message, and supporter counter
6. Featured Action section with call to action
7. Event section with two upcoming event cards
8. Latest News section with three latest blog post
9. Support our work (donation) section
10. Worker and Member Stories Section with feed of social posts
11. Footer.

You can use text and images from clients existing site or placeholder images and placeholder text.

Please submit as many home page mockups/idea boards as you like. Client will pick the top three and ask for some revisions. If you are selected this will lead to a lot of work for this client.

Project is private please adhere to ArtPlenary terms of use and do not share any materials please.

QUICKEST RESPONSE PLEASE!

Thanks for looking!

Target Market(s)

Non profit donors and farmworker advocates

Number of Pages Required

2 page

Font styles to use
Sans Serif

Requirements
Must have
• Adhere to brief and client brand ID
Nice to have
• World class design

```html
<!DOCTYPE html>
<html lang="en">
<head>
<meta charset="utf-8">
<title>Campo Unido Foundation — Home</title>
<link rel="stylesheet" href="https://fonts.googleapis.com/css2?family=Poppins:ital,wght@0,400;0,500;0,600;0,700;0,800;1,400&display=swap">
<style>
:root{
  --red:#d90000;
  --teal:#0e9a9b;
  --ink:#111111;
  --body:#555555;
  --beige:#fae6b3;
  --card:#f4f4f4;
  --white:#ffffff;
  --black:#000000;
}
*{box-sizing:border-box;margin:0;padding:0}
html,body{width:1200px;height:5305px;overflow:hidden}
body{font-family:'Poppins',sans-serif;color:var(--ink);background:var(--white);position:relative}
section,header,footer,.alert-bar{position:relative;width:1200px;overflow:hidden}
.abs{position:absolute}
.photo{position:absolute}

/* alert */
.alert-bar{height:41px;background:var(--teal);color:var(--white);font-size:11px;font-weight:500;text-align:center;line-height:41px}

/* nav */
.site-nav{height:134px;background:var(--white)}
.brand{left:86px;top:40px;display:flex;align-items:center;gap:14px}
.brand-dot{width:56px;height:56px;border-radius:50%;background:var(--red)}
.brand-name{font-size:26px;font-weight:700;line-height:28px;color:var(--ink)}
.main-menu{left:461px;top:58px;display:flex;gap:20px;list-style:none;font-size:11px;font-weight:500;color:#555}
.main-menu .active{color:var(--red)}
.btn-donate{left:850px;top:47px;width:128px;height:42px;border-radius:21px;background:var(--red);color:var(--white);font-size:11px;font-weight:700;text-align:center;line-height:42px}
.btn-language{left:992px;top:47px;width:126px;height:42px;border-radius:21px;border:2px solid var(--red);color:var(--red);font-size:11px;font-weight:700;text-align:center;line-height:38px}

/* hero */
.hero{height:603px}
.hero .photo{inset:0;background:linear-gradient(90deg,#4a4a22 0%,#6d6a3a 35%,#8a7b56 60%,#5c5a34 100%)}
.hero-title{left:97px;top:148px;font-size:50px;font-weight:800;line-height:62px;color:var(--white);letter-spacing:.5px}
.hero-title .accent{color:var(--red)}
.hero-text{left:97px;top:380px;width:420px;font-size:12px;line-height:21px;color:var(--white)}

/* signup */
.signup{height:241px;background:var(--red);color:var(--white)}
.signup h2{left:97px;top:20px;font-size:30px;font-weight:800;letter-spacing:.3px}
.signup .sub{left:97px;top:62px;font-size:11px;font-weight:500}
.email-field{left:395px;top:35px;width:342px;height:38px;border:1.5px solid var(--white);border-radius:19px;font-size:12px;line-height:35px;padding-left:20px}
.btn-signup{left:745px;top:35px;width:128px;height:38px;border-radius:19px;background:var(--white);color:var(--ink);font-size:11px;font-weight:700;text-align:center;line-height:38px}
.signin-label{left:916px;top:46px;font-size:11px;font-weight:500}
.social{top:38px;width:32px;height:32px;border-radius:50%;background:var(--white)}
.signup .rule{left:97px;top:117px;width:1000px;height:1px;background:rgba(255,255,255,.45)}
.text-line{left:0;top:148px;width:1200px;text-align:center;font-size:11px;font-weight:500}
.text-line strong{font-size:20px;font-weight:700;margin-left:10px}
.disclaimer{left:0;top:182px;width:1200px;text-align:center;font-size:11px;font-weight:500}

/* section headings */
.section-title{font-size:30px;font-weight:800;text-align:center;width:1200px;left:0}
.title-rule{width:64px;height:2px;background:var(--red)}
.section-sub{left:330px;width:540px;text-align:center;font-size:11.5px;line-height:21px;color:var(--body)}

/* welcome */
.welcome{height:580px}
.welcome .photo{left:99px;top:129px;width:395px;height:321px;background:linear-gradient(160deg,#5f7e3b,#8ea75a 45%,#c42a22 75%,#6d7f40)}
.welcome h2{left:580px;top:120px;font-size:28px;font-weight:800}
.welcome .title-rule{left:580px;top:177px;width:90px}
.welcome-copy{left:580px;top:212px;width:495px;font-size:11.5px;line-height:20.5px;color:var(--body)}
.welcome-copy p+p{margin-top:20px}

/* featured */
.featured{height:665px;background:linear-gradient(var(--teal) 0 325px,var(--white) 325px)}
.featured .section-title{top:56px;color:var(--white)}
.featured .title-rule{left:568px;top:110px;background:var(--white)}
.featured .section-sub{top:135px;color:var(--white)}
.action-card{top:224px;width:317px}
.action-card .photo{position:relative;height:198px}
.action-card h3{margin-top:28px;font-size:14px;font-weight:600}
.action-card p{margin-top:36px;font-size:11.5px;line-height:21px;color:var(--body);width:260px}
.read-more{display:block;font-size:10.5px;font-weight:700;color:var(--red);margin-top:22px;padding-left:3px}

/* cta */
.cta-band{height:212px;background:var(--red)}
.cta-box{top:43px;width:453px;height:132px;border:1.5px solid rgba(255,255,255,.8);color:var(--white)}
.cta-box .photo{left:18px;top:12px;width:113px;height:107px}
.cta-box h3{left:156px;top:26px;font-size:14px;font-weight:600}
.cta-box p{left:156px;top:60px;width:260px;font-size:11px;line-height:22px}

/* news */
.news{height:714px}
.news .section-title{top:92px}
.news .title-rule{left:568px;top:150px}
.news .section-sub{top:174px}
.post{top:259px;width:318px}
.post .photo{position:relative;height:204px}
.post-meta{margin-top:17px;font-size:10.5px;color:var(--red);font-style:italic}
.post-meta span{color:#777}
.post-meta .date{margin-left:36px}
.post .title-rule{margin-top:10px;width:44px}
.post h3{margin-top:14px;font-size:14px;font-weight:600;line-height:23px;width:300px}

/* partners */
.partners{height:175px;background:var(--beige)}
.partner{top:52px;width:72px;height:72px;border-radius:50%;background:#b9483b;opacity:.55}
.partner.square{border-radius:4px;height:50px;top:63px;background:#4e6b9a}

/* events */
.events{height:735px}
.events .section-title{top:58px}
.events .title-rule{left:568px;top:114px}
.events .section-sub{top:137px}
.event-card{top:224px;width:318px}
.event-card .photo{position:relative;height:342px}
.event-label{height:62px;background:var(--red);color:var(--white);font-size:14px;font-weight:600;text-align:center;line-height:62px}

/* stories */
.stories{height:603px}
.stories .section-title{top:88px}
.stories .title-rule{left:568px;top:146px}
.stories .section-sub{left:230px;width:740px;top:170px}
.story{top:253px;width:482px;height:185px;background:var(--card)}
.story .quote-mark{left:56px;top:30px;font-size:52px;font-weight:800;color:var(--red);line-height:1;font-style:italic}
.story blockquote{position:absolute;left:125px;top:40px;width:320px;font-size:11px;font-style:italic;line-height:20.5px;color:var(--body)}
.member{top:452px;display:flex;align-items:center;gap:22px}
.avatar{width:70px;height:70px;border-radius:50%;background:linear-gradient(135deg,#c9c3bb,#6f6a66)}
.member-name{font-size:14px;font-weight:600}
.member-email{font-size:11px;color:var(--red)}

/* footer */
.site-footer{height:362px;background:var(--black);color:var(--white)}
.site-footer .brand{left:97px;top:72px;position:absolute}
.site-footer .brand-dot{width:52px;height:52px}
.site-footer .brand-name{color:var(--white);font-size:20px;line-height:22px}
.footer-about{left:97px;top:150px;width:460px;font-size:11px;line-height:20.5px}
.copyright{left:97px;top:266px;font-size:11px}
.footer-col h4{font-size:14px;font-weight:600}
.footer-col .title-rule{margin-top:8px;width:48px}
.footer-col ul{list-style:none;margin-top:52px;font-size:10.5px;font-weight:500}
.footer-col li{height:30px}
.footer-phone{left:866px;top:254px;display:flex;align-items:center;gap:12px}
.footer-phone small{display:block;font-size:9px;font-weight:600}
.footer-phone strong{font-size:16px;font-weight:600}
</style>
</head>
<body>

<div class="alert-bar">Neque porro quisquam est qui dolorem ipsum quia dolor sit amet, consectetur, adipisci velit...</div>

<header class="site-nav">
  <div class="brand abs"><span class="brand-dot"></span><span class="brand-name">CAMPO UNIDO<br>FOUNDATION</span></div>
  <ul class="main-menu abs">
    <li class="active">ABOUT US</li><li>IMMIGRATION</li><li>PROGRAMS</li><li>JOIN US</li><li>BLOG</li>
  </ul>
  <a class="btn-donate abs">DONATE NOW</a>
  <a class="btn-language abs">LANGUAGE</a>
</header>

<section class="hero">
  <div class="photo" role="img" aria-label="Smiling farmer holding a basket of fresh vegetables in a green field"></div>
  <h1 class="hero-title abs"><span class="accent">JOIN THE</span><br>FARM WORKER<br>MOVEMENT</h1>
  <p class="hero-text abs">We received thousands of messages and calls expressing interest in applying for the Essential Project's financial assistance opportunity presented by the Campo Unido Foundation.</p>
</section>

<section class="signup">
  <h2 class="abs">STAY INFORMED</h2>
  <p class="sub abs">Sign Up With Email</p>
  <div class="email-field abs">name@example.com</div>
  <a class="btn-signup abs">SIGN UP</a>
  <span class="signin-label abs">Or Sign In With</span>
  <span class="social abs" style="left:1009px" role="img" aria-label="Social sign-in option"></span>
  <span class="social abs" style="left:1069px" role="img" aria-label="Social sign-in option"></span>
  <div class="rule abs"></div>
  <p class="text-line abs">Sign Up With Text <strong>Text "PAPELES" to 555-010</strong></p>
  <p class="disclaimer abs">CUF does not charge for text messages but your phone company may apply charges according to your plan</p>
</section>

<section class="welcome">
  <div class="photo" role="img" aria-label="Woman in a red shirt standing in a vineyard"></div>
  <h2 class="abs">WELCOME</h2>
  <div class="title-rule abs"></div>
  <div class="welcome-copy abs">
    <p>The Campo Unido Foundation is a dynamic nonprofit organization established in 2006. The Campo Unido Foundation's core purpose is to empower communities to ensure human dignity. We serve over 90,000 immigrants annually through a holistic approach; we provide critical services and engage our constituents in systemic change to break the cycle of poverty.</p>
    <p>Our regional offices are safe havens that provide resources and services—such as credible immigration legal advice—and act as hubs for educational outreach and organizing. In addition, our organization works to civically engage farmworkers and Latinos nationally in the democratic process by telling their story, voting and advocating for more equitable policies. The Campo Unido Foundation also provides learning opportunities for members, community fellows, interns, and volunteers.</p>
  </div>
</section>

<section class="featured">
  <h2 class="section-title abs">FEATURED ACTIONS</h2>
  <div class="title-rule abs"></div>
  <p class="section-sub abs">The Campo Unido Foundation is a dynamic nonprofit organization established in 2006. The Campo Unido Foundation's core purpose is to empower communities</p>
  <article class="action-card abs" style="left:97px">
    <div class="photo" role="img" aria-label="Construction worker in a hard hat at a building site" style="background:linear-gradient(135deg,#c9a06a,#e8c08a 50%,#7a94b0)"></div>
    <h3>Worker Rights</h3>
    <p>The Campo Unido Foundation is a dynamic nonprofit organization established in 2006.</p>
    <a class="read-more">READ MORE</a>
  </article>
  <article class="action-card abs" style="left:438px">
    <div class="photo" role="img" aria-label="Smiling older woman wearing glasses" style="background:linear-gradient(135deg,#e9e6e1,#cfc8bf 60%,#b9b3ab)"></div>
    <h3>Public Benefits</h3>
    <p>The Campo Unido Foundation is a dynamic nonprofit organization established in 2006.</p>
    <a class="read-more">READ MORE</a>
  </article>
  <article class="action-card abs" style="left:774px">
    <div class="photo" role="img" aria-label="Caregiver laughing with an elderly woman" style="background:linear-gradient(135deg,#d8d2c6,#bfb6a8 50%,#e1c3a6)"></div>
    <h3>Health</h3>
    <p>The Campo Unido Foundation is a dynamic nonprofit organization established in 2006.</p>
    <a class="read-more">READ MORE</a>
  </article>
</section>

<section class="cta-band">
  <div class="cta-box abs" style="left:115px">
    <div class="photo" role="img" aria-label="Portrait of a smiling young woman" style="background:linear-gradient(135deg,#9aa0a3,#c7b39b)"></div>
    <h3 class="abs">Title is Here</h3>
    <p class="abs">Lorem Ipsum is simply dummy text of the printing and typesetting ustry.</p>
  </div>
  <div class="cta-box abs" style="left:624px">
    <div class="photo" role="img" aria-label="Portrait of a laughing young woman" style="background:linear-gradient(135deg,#d7d0c6,#8a6a52)"></div>
    <h3 class="abs">Title Here</h3>
    <p class="abs">Lorem Ipsum is simply dummy text of the printing and typesetting ustry.</p>
  </div>
</section>

<section class="news">
  <h2 class="section-title abs">LATEST NEWS AND BLOGS</h2>
  <div class="title-rule abs"></div>
  <p class="section-sub abs">The Campo Unido Foundation is a dynamic nonprofit organization established in 2006. The Campo Unido Foundation's core purpose is to empower</p>
  <article class="post abs" style="left:97px">
    <div class="photo" role="img" aria-label="Farm worker in a straw hat harvesting leafy greens" style="background:linear-gradient(135deg,#d2c9a7,#6d9a48 55%,#3e6a2c)"></div>
    <p class="post-meta">Posted by: <span>Thomas</span><span class="date" style="color:var(--red)">Date: </span><span>October 07, 2019</span></p>
    <div class="title-rule"></div>
    <h3>In Kansas and Missouri, Immigrants are Rooted in the Agriculture Workforce</h3>
    <a class="read-more">READ MORE</a>
  </article>
  <article class="post abs" style="left:440px">
    <div class="photo" role="img" aria-label="Worker in a white hard hat and safety vest on site" style="background:linear-gradient(135deg,#cfd7df,#e8a04a 55%,#6f7883)"></div>
    <p class="post-meta">Posted by: <span>Thomas</span><span class="date" style="color:var(--red)">Date: </span><span>October 07, 2019</span></p>
    <div class="title-rule"></div>
    <h3>As temperatures climb, a new push to keep workers safe</h3>
    <a class="read-more">READ MORE</a>
  </article>
  <article class="post abs" style="left:782px">
    <div class="photo" role="img" aria-label="Green rural valley with a small village" style="background:linear-gradient(180deg,#dfe9f0,#7ea55a 40%,#4d7b34)"></div>
    <p class="post-meta">Posted by: <span>Thomas</span><span class="date" style="color:var(--red)">Date: </span><span>October 07, 2019</span></p>
    <div class="title-rule"></div>
    <h3>Something Special Is Happening in Rural America</h3>
    <a class="read-more">READ MORE</a>
  </article>
</section>

<section class="partners" aria-label="Partner organizations">
  <span class="partner square abs" style="left:165px;width:84px"></span>
  <span class="partner abs" style="left:297px"></span>
  <span class="partner abs" style="left:419px;background:#5f8a4a"></span>
  <span class="partner abs" style="left:544px;background:#8a5a2a"></span>
  <span class="partner square abs" style="left:678px"></span>
  <span class="partner abs" style="left:812px;background:#8a8a8a"></span>
  <span class="partner square abs" style="left:946px;width:88px;background:#a33a2c"></span>
</section>

<section class="events">
  <h2 class="section-title abs">PEASANT EVENTS</h2>
  <div class="title-rule abs"></div>
  <p class="section-sub abs">The Campo Unido Foundation is a dynamic nonprofit organization established in 2006. The Campo Unido Foundation's core purpose is to empower</p>
  <article class="event-card abs" style="left:97px">
    <div class="photo" role="img" aria-label="Ladle serving soup into a bowl from a large pot" style="background:linear-gradient(160deg,#5b6b3a,#c8b98a 45%,#c79a3a 75%,#6a5a3a)"></div>
    <div class="event-label">Meals Distribution</div>
  </article>
  <article class="event-card abs" style="left:440px">
    <div class="photo" role="img" aria-label="Hands holding a small globe" style="background:linear-gradient(160deg,#f1efec,#d9cbbd 45%,#6f9ac1 70%,#e2c6ae)"></div>
    <div class="event-label">Citizenship</div>
  </article>
  <article class="event-card abs" style="left:782px">
    <div class="photo" role="img" aria-label="Person carrying a stack of bricks on their shoulder" style="background:linear-gradient(160deg,#f2f2f2,#cfc6bb 40%,#4e6a8f 75%,#2f3c52)"></div>
    <div class="event-label">Labor Rights</div>
  </article>
</section>

<section class="stories">
  <h2 class="section-title abs">OUR MEMBER STORIES</h2>
  <div class="title-rule abs"></div>
  <p class="section-sub abs">The Campo Unido Foundation is a dynamic nonprofit organization established in 2006. The Campo Unido Foundation's core purpose is to empower communities to ensure human dignity. We serve over 90,000 immigrants annually through</p>
  <div class="story abs" style="left:97px">
    <span class="quote-mark abs">“</span>
    <blockquote>These workers – mostly from Mexico – tend to the apple orchards in Waverly, Missouri. This orchard is just a small bite of the area's bountiful agricultural industry – ranging from beef, chicken and milk to apples and peaches – that is largely picked, pruned or packed by an immigrant.</blockquote>
  </div>
  <div class="member abs" style="left:125px">
    <span class="avatar" role="img" aria-label="Member portrait"></span>
    <div><div class="member-name">Reed Calloway</div><div class="member-email">producer@riverbend.org</div></div>
  </div>
  <div class="story abs" style="left:613px">
    <span class="quote-mark abs">“</span>
    <blockquote>These workers – mostly from Mexico – tend to the apple orchards in Waverly, Missouri. This orchard is just a small bite of the area's bountiful agricultural industry – ranging from beef, chicken and milk to apples and peaches – that is largely picked, pruned or packed by an immigrant.</blockquote>
  </div>
  <div class="member abs" style="left:645px">
    <span class="avatar" role="img" aria-label="Member portrait"></span>
    <div><div class="member-name">Marisol Ortega-Vance</div><div class="member-email">mortega@riverbend.org</div></div>
  </div>
</section>

<section class="signup">
  <h2 class="abs">STAY INFORMED</h2>
  <p class="sub abs">Sign Up With Email</p>
  <div class="email-field abs">name@example.com</div>
  <a class="btn-signup abs">SIGN UP</a>
  <span class="signin-label abs">Or Sign In With</span>
  <span class="social abs" style="left:1009px" role="img" aria-label="Social sign-in option"></span>
  <span class="social abs" style="left:1069px" role="img" aria-label="Social sign-in option"></span>
  <div class="rule abs"></div>
  <p class="text-line abs">Sign Up With Text <strong>Text "PAPELES" to 555-010</strong></p>
  <p class="disclaimer abs">CUF does not charge for text messages but your phone company may apply charges according to your plan</p>
</section>

<footer class="site-footer">
  <div class="brand"><span class="brand-dot" style="background:var(--white)"></span><span class="brand-name">CAMPO UNIDO<br>FOUNDATION</span></div>
  <p class="footer-about abs">The Campo Unido Foundation is a dynamic nonprofit organization established in 2006. The Campo Unido Foundation's core purpose is to empower communities to ensure human dignity. We serve over 90,000 immigrants annually through a holistic approach; we provide critical services and engage our</p>
  <p class="copyright abs">Copyright © 2020 Campo Unido Foundation</p>
  <div class="footer-col abs" style="left:652px;top:66px">
    <h4>Useful Links</h4>
    <div class="title-rule"></div>
    <ul style="margin-top:40px"><li>ABOUT US</li><li>IMMIGRATION</li><li>PROGRAMS</li><li>JOIN US</li><li>BLOG</li></ul>
  </div>
  <div class="footer-col abs" style="left:866px;top:66px">
    <h4>Other Links</h4>
    <div class="title-rule"></div>
    <ul style="margin-top:40px"><li>Valor Andes Login</li><li>Membership</li><li>Donate</li></ul>
  </div>
  <div class="footer-phone abs">
    <svg width="34" height="34" viewBox="0 0 34 34" aria-hidden="true">
      <circle cx="17" cy="17" r="15.5" fill="none" stroke="#fff" stroke-width="1.5"/>
      <path d="M12 10.5l3 3-1.6 1.8c.9 2 2.4 3.5 4.4 4.4l1.8-1.6 3 3-2 2c-5.2-.6-9.9-5.3-10.6-10.6z" fill="none" stroke="#fff" stroke-width="1.4" stroke-linejoin="round"/>
    </svg>
    <div><small>CALL US AT</small><strong>1-800-555-0142</strong></div>
  </div>
</footer>

</body>
</html>
```